Modern Venture Capital website

Design a modern website for a venture capital firm. This website should be modern and beautiful and be on par with other Venture Capital websites. I have a logo and a hero video I'd like to use. Link to hero video: https://filevault.example-share.net/file/d/9Q_7k2mzp4r8tn0W6XLfQkHa-BvvRNCT/view?usp=share_link

Preference will be given to the best design that combines design with the best images and digital content. That means no generic free stock videos 😅

I currently built a wix website to give you an idea of what content needs to be on the website. Depending on your design it can be 3 pages, or one long page. I will leave it up to you.

WEBSITE: https://marcel58274.sitebuilder-demo.net/my-site-4

Target Market(s)

Mid-career professionals, individuals interested in Venture Capital

Industry/Entity Type

Finance, venture capital, startups

Requirements
Must have
• must use the hero video I have and must use my logo. Must use high quality images that matches the website design - no generic stock images

```html
<!DOCTYPE html>
<html lang="en">
<head>
<meta charset="utf-8">
<title>Moonlit Ventures — Venture Capital for the late night hustlers</title>
<link href="https://fonts.googleapis.com/css2?family=Poppins:wght@300;400;500;600;700;800&display=swap" rel="stylesheet">
<style>
  :root{
    --stage:#e4e4e4;
    --ink:#000000;
    --night:#060508;
    --paper:#ffffff;
    --figure:#e3e3e3;
    --line:#3a3a3a;
    --chip:#e6e6e6;
    --logo-grey:#8d8d8d;
  }
  *{margin:0;padding:0;box-sizing:border-box}
  html,body{width:1200px;height:3261px;overflow:hidden;background:var(--stage);font-family:'Poppins',sans-serif;color:var(--ink)}
  .page{position:absolute;left:198px;top:178px;width:824px;height:2904px;background:var(--paper);overflow:hidden}
  .abs{position:absolute}

  .hero{left:0;top:0;width:824px;height:341px;
    background:linear-gradient(180deg,#0b0a0c 0%,#141011 55%,#2a1a14 82%,#3b2418 100%)}
  .brand{color:var(--paper);font-weight:700;line-height:1}
  .brand .name{display:block;font-size:18px;letter-spacing:-.3px}
  .brand .sub{display:block;font-size:5.5px;letter-spacing:2px;margin-top:1px}
  .nav{left:349px;top:22px;display:flex;gap:20px;font-size:8px;color:var(--paper)}
  .login{left:647px;top:20px;display:flex;align-items:center;gap:7px;font-size:8px;color:var(--paper)}
  .login .dot{width:14px;height:14px;border-radius:50%;background:#555}
  .btn-light{left:711px;top:18px;width:62px;height:19px;background:var(--paper);border-radius:3px;font-size:7.5px;font-weight:500;display:flex;align-items:center;justify-content:center}
  .hero-title{left:0;width:824px;top:126px;text-align:center;color:var(--paper);font-size:38px;line-height:40px;font-weight:300;letter-spacing:-.5px}
  .hero-title b{font-weight:600}
  .hero-sub{left:0;width:824px;top:225px;text-align:center;color:var(--paper);font-size:8.5px;font-weight:600}

  .vc{left:0;top:341px;width:824px;height:770px;background:var(--night);color:var(--paper)}
  .vc h2{position:absolute;left:61px;top:36px;font-size:61px;font-weight:600;letter-spacing:-1.5px;line-height:70px}
  .vc .intro{position:absolute;left:61px;top:122px;width:440px;font-size:9.5px;line-height:15px}
  .feature{position:absolute;left:349px;width:420px}
  .feature svg{position:absolute;left:0;top:0}
  .feature h3{position:absolute;left:75px;top:0;width:112px;font-size:12px;font-weight:600;line-height:18.5px}
  .feature p{position:absolute;left:205px;top:0;width:205px;font-size:9.5px;line-height:15px}
  .rule{position:absolute;height:1px;background:var(--line);width:394px}

  .founders{left:0;top:1111px;width:824px;height:299px;border-bottom:1px solid #e2e2e2;text-align:center}
  .founders h4{margin-top:72px;font-size:12px;font-weight:600}
  .founders p{font-size:9.5px;line-height:15px;margin:0 auto}
  .chip{display:inline-flex;align-items:center;justify-content:center;width:62px;height:20px;background:var(--chip);border-radius:3px;font-size:7.5px;font-weight:500}

  .figure{position:absolute;left:91px}
  .figure .num{display:block;font-size:86px;font-weight:800;color:var(--figure);line-height:78px;letter-spacing:-4px}
  .figure .label{display:block;font-size:11px;font-weight:600;margin-top:2px}
  .fund-title{left:404px;top:1742px;font-size:61px;font-weight:600;line-height:64px;letter-spacing:-1px}

  .partners{left:0;top:2203px;width:824px;height:117px;background:var(--ink);display:flex;justify-content:center;align-items:center;gap:60px;color:var(--logo-grey);font-weight:700;font-size:17px}

  .cta{left:0;top:2320px;width:824px;height:301px;text-align:center}
  .cta h4{margin-top:101px;font-size:11.5px;font-weight:600}
  .cta p{margin-top:18px;font-size:9.5px}

  .footer{left:0;top:2621px;width:824px;height:283px;background:var(--ink);color:var(--paper)}
  .footer .contact{position:absolute;left:93px;top:131px;font-size:9.5px;line-height:15px}
  .footer .contact u{text-decoration:underline}
  .footer .copy{position:absolute;left:93px;top:214px;font-size:9.5px}
  .footer .pages{position:absolute;left:311px;top:84px}
  .footer h5{font-size:11px;font-weight:600}
  .footer .pages a{display:block;color:var(--paper);text-decoration:none;font-size:9.5px;line-height:23px}
  .footer .news{position:absolute;left:458px;top:70px;width:190px}
  .field{margin-top:12px;width:135px;height:21px;border:1px solid var(--paper);border-radius:3px;font-size:7.5px;padding:3px 5px}
  .check{margin-top:11px;display:flex;gap:8px;font-size:9px;line-height:13px;width:150px}
  .check span.box{flex:none;width:8px;height:8px;border:1px solid var(--paper);margin-top:3px}
  .submit{margin-top:9px;width:135px;height:20px;background:var(--paper);color:var(--ink);border-radius:3px;font-size:8px;font-weight:500;display:flex;align-items:center;justify-content:center}
  .social{position:absolute;left:673px;top:134px;display:flex;gap:3px}
  .social span{width:18px;height:18px;border-radius:50%;background:var(--paper)}
</style>
</head>
<body>
<main class="page">

  <header class="abs hero" role="img" aria-label="Night-time city skyline with lit towers along the lower edge">
  </header>
  <div class="abs brand" style="left:52px;top:20px"><span class="name">Moonlit</span><span class="sub">VENTURES</span></div>
  <nav class="abs nav"><span>Home</span><span>Join VC</span><span>Startups</span></nav>
  <div class="abs login"><span class="dot"></span>Log In</div>
  <div class="abs btn-light">Get Started</div>
  <h1 class="abs hero-title"><b>Venture Capital</b> for the late<br>night hustlers</h1>
  <div class="abs hero-sub">Become A Venture Capital Investor</div>

  <section class="abs vc">
    <h2>Become a VC</h2>
    <p class="intro">At Moonlit Ventures, we’re opening the doors to a new kind of investor, mid-career professionals and aspiring VCs who want real skin in the game, not just exposure from the sidelines.</p>

    <div class="feature" style="top:197px">
      <svg width="56" height="42" viewBox="0 0 56 42"><path d="M14 40h28a13 13 0 0 0 2-26A17 17 0 0 0 12 18 11 11 0 0 0 14 40z" fill="#fff"/></svg>
      <h3 style="width:90px">Hands on VC Work</h3>
      <p>Each Moonlit Investor can actively be involved in sourcing, evaluating, and making key investment decisions as little or as much as they want.</p>
    </div>
    <div class="rule" style="left:348px;top:281px"></div>

    <div class="feature" style="top:325px">
      <svg width="56" height="42" viewBox="0 0 56 42"><path d="M2 6c18 6 34-6 52 0v30c-18-6-34 6-52 0z" fill="#fff"/><ellipse cx="28" cy="21" rx="7" ry="9" fill="#060508"/></svg>
      <h3>Earn Carry and Put Your Name on an Investment</h3>
      <p style="left:216px">Earn carry interest based on the level of your involvement on each deal.</p>
    </div>
    <div class="rule" style="left:342px;top:411px"></div>

    <div class="feature" style="top:450px">
      <svg width="56" height="52" viewBox="0 0 56 52"><circle cx="26" cy="24" r="24" fill="#fff"/></svg>
      <h3>Meaningful Opportunities to develop your career in Venture Capital</h3>
      <p>Moonlit Investors, depending on the level of commitment and involvement, can work at our fund as Partners, Principals, Senior Associates, Associates and Venture Partners.</p>
    </div>
    <div class="rule" style="left:348px;top:565px"></div>

    <div class="feature" style="top:615px">
      <svg width="56" height="52" viewBox="0 0 56 52"><circle cx="20" cy="11" r="10" fill="#fff"/><path d="M2 50c0-16 8-24 18-24s18 8 18 24z" fill="#fff"/></svg>
      <h3 style="width:95px">Join a community of Hustlers</h3>
      <p style="left:190px;width:170px">Network with likeminded investors, aspiring investors and limited partners.</p>
    </div>
  </section>

  <section class="abs founders">
    <h4>Simplifying success for founders</h4>
    <p style="margin-top:20px;width:585px">Our strength lies in our network. Our LPs and operating partners are all mid-to-senior level executives in their industries. They bring real-world corporate experience, offering strategic insights and operational support to help our portfolio companies scale efficiently.</p>
    <p style="margin-top:14px;width:535px">We cut through the noise and get to the core of your business fast. If we love what you’re building, we’ll move. If not, we’ll tell you quickly and respectfully. That lets you make</p>
    <div style="margin-top:20px"><span class="chip">Learn More</span></div>
  </section>

  <div class="figure" style="top:1495px"><span class="num">14</span><span class="label">Pre-Seed / Seed Investments</span></div>
  <div class="figure" style="top:1626px"><span class="num">50K</span><span class="label">Check Size</span></div>
  <div class="figure" style="top:1757px"><span class="num">20%</span><span class="label">Carried Interest</span></div>
  <div class="figure" style="top:1888px"><span class="num">2.5%</span><span class="label">Management Fee</span></div>
  <div class="figure" style="top:2018px"><span class="num">1M</span><span class="label">Fund Size</span></div>
  <h2 class="abs fund-title">Fund<br>Economics</h2>

  <section class="abs partners">
    <span>KORVEL</span><span>Quenrow</span><span>Brindle</span><span>TESSIO</span>
  </section>

  <section class="abs cta">
    <h4>Ready to start investing as a VC?</h4>
    <p>Book an interview to learn more and see if you qualify.</p>
    <div style="margin-top:17px"><span class="chip">Get Started</span></div>
  </section>

  <footer class="abs footer">
    <div class="abs brand" style="left:97px;top:72px"><span class="name">Moonlit</span><span class="sub">VENTURES</span></div>
    <div class="contact">555-014-2290<br><u>hello@moonlitvc.example</u><br>210 Harbor Lane<br>Oakview, CA 94021</div>
    <div class="copy">© 2025 Moonlit Ventures</div>
    <div class="pages">
      <h5>Pages</h5>
      <div style="margin-top:12px"><a>Solutions</a><a>Vision</a><a>Programs</a><a>Blog</a></div>
    </div>
    <div class="news">
      <h5>Subscribe to Our Newsletter</h5>
      <div class="field">Email</div>
      <div class="check"><span class="box"></span><span>Yes, subscribe me to your newsletter.*</span></div>
      <div class="submit">Submit</div>
    </div>
    <div class="social"><span></span><span></span><span></span></div>
  </footer>

</main>
</body>
</html>
```